8" x 11" One Page Flyer for Fence Installation Company

We are looking to promote our business with a new flyer that would be handed out in person to people or put at their mailbox/door at their homes. The flyer needs to be creative and attention-grabbing. I have attached some of our previous flyers and our website information. Do not call or email regarding the flyer. We want the flyer to look professional but also friendly. One page, NOT folded. You can use images from our website at www.MyBraxtonYard.com or our Facebook page at www.Facebook.com/HollowbrookRailsBKT. We are flexible with what photos you can use but there must be photos of OUR fences on the flyer. More photos specifically can also be provided. Colors need to be suitable for a flyer printed on canary yellow in color paper OR white paper.

Target Market(s)

Homeowners that need a new fence

Industry/Entity Type

Construction

Font styles to use
Sans Serif
Other font styles liked:
• HD Colton

Colors
0054AA
0677BA
7BADD7
CADEEF
E8F1F8
0094D4
00A9DD
6FCCEA
C7EBF8
E9F6FB

Requirements
Must have
• Our fence photos - mostly wood fence photos (different designs), SIZE SHOULD BE LETTER SIZE 8" x 11"
Nice to have
• A nice bible verse featured at the bottom of the flyer.
Should not have
• DO NOT COPY THE WEBSITE FORMAT, I WANT SOMETHING UNIQUE. Other people's fence photos, they must all come from our website or facebook page

```html
<!DOCTYPE html>
<html lang="en">
<head>
<meta charset="UTF-8">
<title>Hollowbrook Rails – Fence Flyer</title>
<link rel="stylesheet" href="https://fonts.googleapis.com/css2?family=Lexend:wght@400;600;700&family=Questrial&display=swap">
<style>
  :root{
    --bg:#e6e6e6;
    --paper:#ffffff;
    --paper-shade:#f1f1f1;
    --orange:#f39a2a;
    --orange-deep:#ee8a1c;
    --brown:#4a1c10;
    --ink:#1e1e1e;
    --blue:#3a8fd9;
    --band:#6b4a35;
    --band-light:#8a6a52;
    --footer:#ececec;
    --body:"Questrial", sans-serif;
    --head:"Lexend", sans-serif;
  }
  *{margin:0;padding:0;box-sizing:border-box}
  html,body{width:1200px;height:900px;overflow:hidden;background:var(--bg)}
  .flyer{
    position:absolute;left:290px;top:20px;width:620px;height:860px;
    background:linear-gradient(180deg,var(--paper) 0%,var(--paper) 60%,var(--paper-shade) 100%);
    box-shadow:0 2px 10px rgba(0,0,0,.15);overflow:hidden;font-family:var(--body);color:var(--ink);
  }
  .shapes{position:absolute;left:0;top:0}
  .t{position:absolute;white-space:nowrap}
  .brand-mark{position:absolute;left:24px;top:335px;width:44px;height:44px;background:var(--brown)}
  .brand-name{left:80px;top:330px;font-family:var(--head);font-weight:600;font-size:19px;color:var(--blue)}
  .brand-phone{left:80px;top:354px;font-family:var(--head);font-weight:700;font-size:18px;color:var(--ink)}
  .brand-tagline{left:80px;top:380px;font-size:6.5px;color:var(--ink)}
  .headline{left:24px;top:420px;font-family:var(--head);font-weight:700;font-size:21px;color:var(--brown)}
  .headline .accent{color:var(--orange);font-size:28px}
  .subhead{left:28px;top:455px;font-family:var(--head);font-size:13.5px;color:var(--ink)}
  .why-label{left:34px;top:499px;font-family:var(--head);font-weight:600;font-size:14px;color:var(--brown)}
  .intro{left:34px;top:529px;font-family:var(--head);font-size:12.5px;color:var(--ink)}
  .features{position:absolute;top:558px;list-style:none;font-family:var(--head);font-size:9.5px;color:var(--ink)}
  .features li{height:20px;line-height:14px;padding-left:14px;position:relative}
  .features li::before{content:"";position:absolute;left:0;top:4px;width:7px;height:7px;background:var(--orange-deep)}
  .features.left{left:34px}
  .features.right{left:236px}
  .divider{position:absolute;left:222px;top:560px;width:1px;height:76px;background:#bbb}
  .showroom-title{left:33px;top:656px;font-family:var(--head);font-size:18px;color:var(--ink)}
  .showroom-text{left:33px;top:684px;font-family:var(--head);font-size:12px;color:var(--ink)}
  .hours{left:33px;top:703px;font-family:var(--head);font-weight:700;font-size:16.5px;color:var(--brown)}
  .verse{position:absolute;left:132px;top:760px;width:480px;font-size:7.3px;line-height:1.45;color:#fff}
  .contact{top:833px;font-family:var(--head);font-size:11px;color:var(--ink)}
  .contact.call{left:35px}
  .contact.mail{left:212px}
  .contact.web{left:440px}
</style>
</head>
<body>
<main class="flyer">
  <svg class="shapes" width="620" height="860" viewBox="0 0 620 860">
    <polygon class="corner-accent" points="0,0 335,0 0,318" fill="#f39a2a"/>
    <polygon role="img" aria-label="Photo: backyard patio with umbrella enclosed by a new wooden picket fence" points="335,0 620,0 620,376 570,423 245,88" fill="#a8b87a" stroke="#fff" stroke-width="5"/>
    <polygon role="img" aria-label="Photo: wooden split rail fence in a yard" points="238,100 353,215 238,330 123,215" fill="#8aa864" stroke="#fff" stroke-width="5"/>
    <polygon role="img" aria-label="Photo: black metal fence around a lawn" points="365,211 483,329 365,447 247,329" fill="#5f7d45" stroke="#fff" stroke-width="5"/>
    <polygon role="img" aria-label="Photo: wooden gate in a split rail fence" points="488,347 600,459 488,571 376,459" fill="#b7a77a" stroke="#fff" stroke-width="5"/>
    <polygon class="why-banner" points="24,494 206,494 196,520 24,520" fill="#f39a2a"/>
    <rect class="verse-band" x="0" y="749" width="620" height="73" fill="#6b4a35"/>
    <rect role="img" aria-label="Photo: three crosses on a hillside at dusk" x="0" y="749" width="128" height="73" fill="#9c8470"/>
    <rect class="contact-bar" x="0" y="822" width="620" height="38" fill="#ececec"/>
  </svg>

  <div class="brand-mark"></div>
  <div class="t brand-name">Hollowbrook Rails</div>
  <div class="t brand-phone">555-014-2290</div>
  <div class="t brand-tagline">"Because Good Fences Make Good Neighbors"</div>

  <h1 class="t headline">WE BUILD <span class="accent">FENCES....</span></h1>
  <p class="t subhead">And we would love to build your fence too!</p>

  <h2 class="t why-label">WHY CHOOSE US?</h2>
  <p class="t intro">Beautiful, professionally installed fences at affordable</p>

  <ul class="features left">
    <li>Free Estimates</li>
    <li>Professional Installation</li>
    <li>Concrete in EVERY Post</li>
    <li>HOA Submission Assistance</li>
  </ul>
  <div class="divider"></div>
  <ul class="features right">
    <li>Lifetime Workmanship Warranty</li>
    <li>Experienced Installation Teams</li>
    <li>Quality Workmanship &amp; Materials</li>
    <li>FREE Gate Adjustments for LIFE</li>
  </ul>

  <h2 class="t showroom-title">Visit our indoor &amp; outdoor showroom!</h2>
  <p class="t showroom-text">Our outdoor showroom is open 24/7, while our indoor showroom and office is open</p>
  <p class="t hours">MONDAY - THURS 9AM - 3PM, FRIDAY 9AM - 1PM</p>

  <p class="verse">So do not fear, for I am with you; do not be dismayed, for I am your God. I will strengthen you and help you; I will uphold you with my righteous right hand." Do not be anxious about anything, but in every situation, by prayer and petition, with thanksgiving, present your requests to God.</p>

  <p class="t contact call">CALL US - 555-014-2290</p>
  <p class="t contact mail">MAIL US -office@mybraxtonyard.com</p>
  <p class="t contact web">www.MyBraxtonYard.com</p>
</main>
</body>
</html>
```